Hip, Modern Home Page for Successful SEO Expert

Marcus Delwyn is an SEO expert, author and professional speaker. His site is
www.marcusdelwyn.net. We need a re-design of the website so that it does not look outdated or like an off-the-shelf Pressmark template (like it currently does). The new design must convey to the visitor a compelling call-to-action. Specially, this home page will act as a “squeeze page” and thus, the primary marketing goal will be to get the user to opt in to our list. The new design will provide elements of “social proof” such as written testimonials, a portfolio of case studies, client logos, “as appeared on” logos, client testimonial video, etc.
Updates

Please incorporate the recently uploaded headshots into your design 

Target Market(s)

People looking for help in internet marketing for their websites, entrepreneurs, start-ups, bloggers, companies looking to build an online presence, conferences looking to book Marcus for speaking. Small business people and SEO newbies interested in buying Marcus’s video-based training (RankCraftLab.net).

Industry/Entity Type

Marketing

Font styles to use
Sans Serif

Colors
f68d4d
3276b5
8769ae
acd036

Requirements
Must have
• strong call to action
Should not have
• should not look like a template. should not use old style fonts. should not have more than one page scroll

```html
<!DOCTYPE html>
<html lang="en">
<head>
<meta charset="utf-8">
<title>Marcus Delwyn – SEO expert, author, professional speaker</title>
<link rel="stylesheet" href="https://fonts.googleapis.com/css2?family=Open+Sans:wght@400;600;700&family=Arimo:wght@400;700&family=Signika:wght@400&display=swap">
<style>
:root{
  --ink:#1c1c1c;
  --text:#444;
  --muted:#9a9a9a;
  --link:#1a8ad0;
  --band:#6b6b6b;
  --panel-head:#7c7c7c;
  --card:#ececec;
  --card-edge:#c9c9c9;
  --line:#dedede;
  --footer:#0d0d0d;
  --white:#fff;
}
*{margin:0;padding:0;box-sizing:border-box}
html,body{width:894px;height:1200px;overflow:hidden;background:var(--white)}
body{position:relative;font-family:"Arimo",Arial,sans-serif;color:var(--text)}
.abs{position:absolute}

/* header */
.site-header{left:0;top:0;width:894px;height:63px;background:var(--white)}
.brand{left:76px;top:23px}
.brand-name{font-family:"Open Sans",sans-serif;font-weight:700;font-size:15px;letter-spacing:.6px;color:var(--ink);font-variant:small-caps;line-height:1}
.brand-tag{font-size:7.5px;font-weight:700;color:var(--ink);margin-top:2px}
.main-nav{left:318px;top:32px;display:flex;font-size:11.5px;color:var(--ink);white-space:nowrap}
.main-nav span{margin-right:21.5px}
.main-nav .active{color:var(--link)}
.search-icon{left:801px;top:32px}

/* hero */
.hero{left:0;top:63px;width:894px;height:309px;background:linear-gradient(100deg,#b58f5c 0%,#c79a66 30%,#a87d4d 55%,#caa06a 80%,#8f6a44 100%)}
.hero-caption{left:533px;top:200px;width:283px;height:30px;background:rgba(240,240,240,.85);font-family:"Signika",sans-serif;font-size:13.5px;color:#222;text-align:center;line-height:30px;white-space:nowrap}
.hero-dots{left:418px;top:291px;display:flex;gap:6px}
.hero-dots i{display:block;width:10px;height:10px;border-radius:50%;background:#fff}
.hero-dots i.on{background:var(--link)}

/* opt-in band */
.optin-band{left:0;top:372px;width:894px;height:204px;background:var(--band);border-bottom:1px solid #444}
.optin-card{left:72px;top:10px;width:492px;height:184px;background:var(--white);border:1px solid #999}
.book-cover{left:30px;top:16px;width:110px;height:150px;background:linear-gradient(160deg,#f2f2f2 0%,#dfe4ec 45%,#27446e 100%);transform:skewY(-4deg)}
.optin-title{left:173px;top:26px;font-size:13.5px;color:var(--ink);line-height:26px;white-space:nowrap}
.optin-note{left:173px;top:80px;width:300px;font-size:8.5px;color:var(--ink);line-height:16px}
.email-field{left:173px;top:124px;width:181px;height:36px;border:1px solid #c8c8c8;background:#eee;font-size:8.5px;color:#666;padding-left:10px;line-height:34px}
.subscribe{left:363px;top:122px;width:93px;height:38px;background:linear-gradient(#2a9fe0,#167fbe);color:#fff;font-size:12px;text-align:center;line-height:38px;border-radius:2px}

.video-panel{left:573px;top:10px;width:243px;height:183px;background:#111}
.video-head{left:0;top:0;width:243px;height:28px;background:var(--panel-head);color:#fff;font-size:13.5px;text-align:center;line-height:29px}
.video-frame{left:0;top:28px;width:243px;height:155px;background:linear-gradient(180deg,#7f8a6a 0%,#6e7a5f 60%,#2a2a2a 100%)}
.video-title{left:6px;top:4px;font-size:6px;color:#eee}
.play{left:104px;top:60px;width:34px;height:23px;background:rgba(0,0,0,.85);border-radius:5px}
.video-bar{left:0;top:137px;width:243px;height:18px;background:#1a1a1a;font-size:5px;color:#bbb;padding:6px 0 0 40px}

/* section titles */
.sec-title{font-family:"Open Sans",sans-serif;font-size:14px;color:var(--ink);letter-spacing:.2px}
.arrows{display:flex;gap:2px}
.arrows i{display:block;width:16px;height:16px;background:#111;position:relative}
.arrows.light i{background:#9a9a9a}
.arrows i svg{position:absolute;left:4px;top:3px}

/* portfolio */
.portfolio-item{top:619px;width:143px;height:92px}

/* blog */
.blog-card{left:75px;width:383px;height:69px;background:var(--card);border:1px solid var(--card-edge)}
.blog-thumb{left:4px;top:4px;width:77px;height:61px;background:linear-gradient(135deg,#dfe6ee,#8aa0b6 60%,#41526a)}
.blog-title{left:91px;top:6px;font-size:10.5px;color:var(--link);white-space:nowrap}
.blog-date{left:91px;top:19px;font-size:10.5px;color:#111}
.share{top:48px;height:14px;border:1px solid #bbb;background:#fafafa;font-size:8px;font-weight:700;color:#333;line-height:12px;padding:0 5px;border-radius:2px}
.count{top:48px;width:14px;height:14px;border:1px solid #bbb;background:#fff;font-size:7px;text-align:center;line-height:12px}

/* testimonials */
.quote-card{left:493px;width:325px;background:var(--card);border:1px solid #d6d6d6}
.quote-text{left:33px;top:9px;width:280px;font-size:8.8px;line-height:14.2px;color:#555}
.quote-more{color:var(--link)}
.quote-mark{font-family:"Open Sans",sans-serif;font-weight:700;font-size:17px;color:var(--link);line-height:1}

/* logos */
.logo-row{left:72px;top:936px;width:744px;height:73px;border-bottom:1px solid var(--line);display:flex}
.logo-row div{flex:1;border-right:1px solid var(--line);display:flex;align-items:center;justify-content:center;gap:6px;font-family:"Open Sans",sans-serif;font-weight:600;font-size:17px;color:#c4c4c4}
.logo-row div:last-child{border-right:none}
.dot{width:14px;height:14px;border-radius:50%;background:#d0d0d0}
.press-box{left:73px;top:1044px;width:756px;height:61px;border:1px solid #ddd;display:flex;align-items:center;justify-content:space-around;font-family:"Open Sans",sans-serif;font-weight:600;font-size:19px;color:#8a8a8a}
.press-box span{display:flex;align-items:center;gap:6px}
.sq{width:13px;height:13px;background:#9a9a9a}

/* footer */
.site-footer{left:0;top:1113px;width:894px;height:87px;background:var(--footer)}
.copyright{left:76px;top:37px;font-size:8.5px;color:#ccc}
.social{left:376px;top:29px;display:flex;gap:8px}
.social i{display:block;width:26px;height:26px;border-radius:50%;background:radial-gradient(circle at 40% 35%,#6a6a6a,#333);border:1px solid #555}
.newsletter{left:638px;top:33px;width:178px;height:21px;background:#fff;font-size:9px;font-style:italic;color:#666;padding-left:8px;line-height:21px}
.newsletter svg{position:absolute;right:3px;top:3px}
</style>
</head>
<body>

<header class="site-header abs">
  <div class="brand abs">
    <div class="brand-name">Marcus Delwyn</div>
    <div class="brand-tag">SEO expert, author, professional speaker</div>
  </div>
  <nav class="main-nav abs">
    <span class="active">Biography</span><span>Books</span><span>Articles</span><span>Speaking</span><span>Interviews</span><span>Testimonials</span><span>In the News</span>
  </nav>
  <svg class="search-icon abs" width="15" height="15" viewBox="0 0 15 15"><circle cx="6" cy="6" r="4.5" fill="none" stroke="#888" stroke-width="2"/><line x1="9.5" y1="9.5" x2="14" y2="14" stroke="#888" stroke-width="2.4"/></svg>
</header>

<section class="hero abs" role="img" aria-label="Photo of Marcus Delwyn seated at a panel table with laptops and microphones at a conference">
  <div class="hero-caption abs">Marcus Delwyn at SearchSummit West 2011</div>
  <div class="hero-dots abs"><i class="on"></i><i></i><i></i><i></i></div>
</section>

<section class="optin-band abs">
  <div class="optin-card abs">
    <div class="book-cover abs" role="img" aria-label="Cover of the Blog Income Roadmap report"></div>
    <div class="optin-title abs">Learn How To Make $10,000 Per Month<br>Blogging 2 Hours A Day</div>
    <div class="optin-note abs">Enter your email to join my newsletter and download the blog income roadmap exclusive report</div>
    <div class="email-field abs">Enter Your Email</div>
    <div class="subscribe abs">SUBSCRIBE</div>
  </div>
  <div class="video-panel abs">
    <div class="video-head abs">CLIENT TESTIMONIAL VIDEO</div>
    <div class="video-frame abs" role="img" aria-label="Video still of a client speaking to camera">
      <div class="video-title abs">Thinking Clearly About Your Search Plan</div>
      <div class="play abs"><svg width="34" height="23"><polygon points="14,6 22,11.5 14,17" fill="#fff"/></svg></div>
      <div class="video-bar abs">0:00 / 1:06</div>
    </div>
  </div>
</section>

<div class="sec-title abs" style="left:74px;top:593px">PORTFOLIO</div>
<div class="arrows abs" style="left:785px;top:597px">
  <i><svg width="8" height="10"><polyline points="6,1 2,5 6,9" fill="none" stroke="#fff" stroke-width="1.5"/></svg></i>
  <i><svg width="8" height="10"><polyline points="2,1 6,5 2,9" fill="none" stroke="#fff" stroke-width="1.5"/></svg></i>
</div>
<div class="portfolio-item abs" style="left:74px;background:linear-gradient(160deg,#e3c49a,#8b8b8b 70%,#5a6f8a)" role="img" aria-label="Portfolio case study artwork: figure on cracked ground"></div>
<div class="portfolio-item abs" style="left:226px;background:radial-gradient(circle at 50% 45%,#e8a07a,#c2331f 60%,#7a1410)" role="img" aria-label="Portfolio case study artwork: red painted couple"></div>
<div class="portfolio-item abs" style="left:377px;background:linear-gradient(90deg,#111 0%,#555 50%,#111 100%)" role="img" aria-label="Portfolio case study artwork: black and white portrait illustration"></div>
<div class="portfolio-item abs" style="left:527px;background:linear-gradient(120deg,#1d2f4a,#d8465e 40%,#3fb36b 65%,#2b78c2)" role="img" aria-label="Portfolio case study artwork: colourful 3D bars"></div>
<div class="portfolio-item abs" style="left:677px;background:radial-gradient(circle at 60% 55%,#f3b24a,#6b4a1d 50%,#1d1d14)" role="img" aria-label="Portfolio case study artwork: sunset landscape with chapel"></div>

<div class="sec-title abs" style="left:77px;top:723px">BLOG</div>
<div class="arrows light abs" style="left:424px;top:721px">
  <i><svg width="8" height="10"><polyline points="6,1 2,5 6,9" fill="none" stroke="#fff" stroke-width="1.5"/></svg></i>
  <i><svg width="8" height="10"><polyline points="2,1 6,5 2,9" fill="none" stroke="#fff" stroke-width="1.5"/></svg></i>
</div>

<article class="blog-card abs" style="top:748px">
  <div class="blog-thumb abs" role="img" aria-label="Photo of business people in an office"></div>
  <div class="blog-title abs">Telecommunications Companies Eyeball Ghana for 2014</div>
  <div class="blog-date abs">January 24, 2014</div>
  <div class="share abs" style="left:92px">Save</div><div class="count abs" style="left:123px">0</div>
  <div class="share abs" style="left:168px">Post</div><div class="count abs" style="left:196px">0</div>
  <div class="share abs" style="left:251px">Share</div>
</article>
<article class="blog-card abs" style="top:825px">
  <div class="blog-thumb abs" role="img" aria-label="Photo of business people in an office"></div>
  <div class="blog-title abs">Telecommunications Companies Eyeball Ghana for 2014</div>
  <div class="blog-date abs">January 24, 2014</div>
  <div class="share abs" style="left:92px">Save</div><div class="count abs" style="left:123px">0</div>
  <div class="share abs" style="left:168px">Post</div><div class="count abs" style="left:196px">0</div>
  <div class="share abs" style="left:251px">Share</div>
</article>

<div class="sec-title abs" style="left:491px;top:723px">TESTIMONIALS</div>
<div class="arrows light abs" style="left:787px;top:720px">
  <i><svg width="8" height="10"><polyline points="6,1 2,5 6,9" fill="none" stroke="#fff" stroke-width="1.5"/></svg></i>
  <i><svg width="8" height="10"><polyline points="2,1 6,5 2,9" fill="none" stroke="#fff" stroke-width="1.5"/></svg></i>
</div>
<blockquote class="quote-card abs" style="top:749px;height:71px">
  <span class="quote-mark abs" style="left:10px;top:12px">&ldquo;</span>
  <p class="quote-text abs">Our Protection Plans will give you the same warranty offered by Orchard Care, Novalink, Kestra and other manufacturers for as long as you'd like. We even extend warranties for older devices! -<br><span class="quote-more">See more</span></p>
  <span class="quote-mark abs" style="left:305px;top:44px">&rdquo;</span>
</blockquote>
<blockquote class="quote-card abs" style="top:823px;height:67px">
  <span class="quote-mark abs" style="left:10px;top:12px">&ldquo;</span>
  <p class="quote-text abs">Our Protection Plans will give you the same warranty offered by Orchard Care, Novalink, Kestra and other manufacturers for as long as you'd like. We even extend warranties for older devices! -<br><span class="quote-more">See more</span></p>
  <span class="quote-mark abs" style="left:305px;top:44px">&rdquo;</span>
</blockquote>

<div class="sec-title abs" style="left:75px;top:913px;font-weight:600">CLIENT LOGOS</div>
<div class="logo-row abs">
  <div>Layerforge</div>
  <div><i class="dot"></i>Nebulon</div>
  <div>Vertexa</div>
  <div>Amberline</div>
  <div><i class="dot"></i>Outframe</div>
</div>

<div class="sec-title abs" style="left:75px;top:1023px;font-weight:600">AS APPEAR ON</div>
<div class="press-box abs">
  <span>Marketvale</span>
  <span><i class="dot" style="background:#9a9a9a"></i>Pressmark</span>
  <span><i class="sq"></i>Themegrove</span>
  <span>Querylite</span>
  <span>Graphbay</span>
</div>

<footer class="site-footer abs">
  <div class="copyright abs">© 2014.&nbsp; Marcus Delwyn. All Rights Reserved</div>
  <div class="social abs" aria-label="Social profiles"><i></i><i></i><i></i><i></i><i></i></div>
  <div class="newsletter abs">NEWS LETTER
    <svg width="26" height="15" viewBox="0 0 26 15"><rect x="1" y="1" width="24" height="13" fill="#222"/><polyline points="1,1 13,9 25,1" fill="none" stroke="#fff" stroke-width="1.5"/></svg>
  </div>
</footer>

</body>
</html>
```